Homecare Information Flyer

We require a brochure/ leaflet to be created which would provide healthcare information to our staff and patients on the topic of- Pressure Ulcers. The document would ideally be 3 fold. It should include our Logo/ Company Information (Marlowe Staffing).

I have attached-
- Logo
- Text/ Visual images to be included.

Industry/Entity Type

Healthcare

```html
<!DOCTYPE html>
<html lang="en">
<head>
<meta charset="utf-8">
<title>Pressure Ulcer Leaflet – Marlowe Staffing</title>
<link rel="stylesheet" href="https://fonts.googleapis.com/css2?family=Arimo:wght@400;700&family=PT+Sans:wght@400&family=Tinos&display=swap">
<style>
  :root {
    --lime: #a9c93c;
    --green: #4b8a2f;
    --dark-green: #3f7d27;
    --pale-yellow: #fbf39c;
    --ink: #1a1a1a;
    --grey: #6b6b6b;
    --paper: #ffffff;
  }
  html, body { margin: 0; padding: 0; overflow: hidden; }
  body { width: 1200px; height: 927px; background: var(--paper); font-family: "Arimo", Arial, sans-serif; color: var(--ink); }
  .leaflet { position: relative; width: 1200px; height: 927px; overflow: hidden; }

  .band { position: absolute; left: 0; width: 400px; margin: 0; background: var(--lime); padding: 3px 8px; box-sizing: border-box; font-weight: 700; font-size: 25px; line-height: 30px; }
  .band--top { top: 12px; height: 64px; }
  .band--top .lead { color: var(--dark-green); }
  .band--top .tail, .band--bottom { color: var(--paper); }
  .band--bottom { top: 720px; height: 66px; }

  .copy { position: absolute; left: 10px; width: 395px; margin: 0; font-family: "PT Sans", "Myriad Pro", sans-serif; font-size: 16.5px; line-height: 20px; white-space: nowrap; }
  .topic { position: absolute; left: 10px; margin: 0; font-size: 24px; line-height: 28px; font-weight: 700; color: var(--green); }

  .tag { position: absolute; margin: 0; background: var(--pale-yellow); color: var(--green); font-weight: 700; display: flex; align-items: center; justify-content: center; }
  .tag--classification { left: 450px; top: 46px; width: 318px; height: 67px; font-size: 26px; }
  .tag--leaflet { left: 843px; top: 590px; width: 267px; height: 47px; font-size: 28px; letter-spacing: 1px; }

  .stage-label { position: absolute; left: 512px; margin: 0; font-size: 25px; font-weight: 700; }
  .stage-label .numeral { font-family: "Tinos", "Times New Roman", serif; font-weight: 400; }
  .stage-diagram { position: absolute; left: 520px; width: 170px; background: linear-gradient(#fdf2a0 0%, #f9c77a 25%, #4b8a2f 40%, #b9d94a 60%, #646464 85%); }

  .brand { position: absolute; left: 832px; top: 255px; width: 286px; text-align: center; }
  .brand-mark { width: 120px; height: 120px; border-radius: 50%; background: var(--green); margin: 0 auto 22px; }
  .brand-name { font-size: 34px; font-weight: 700; color: var(--grey); }

  .talk-icon { position: absolute; left: 930px; top: 665px; width: 165px; height: 155px; background: linear-gradient(135deg, #b7d63e, #3f7d27); border-radius: 10px; }
</style>
</head>
<body>
<main class="leaflet">
  <section class="advice">
    <h1 class="band band--top"><span class="lead">What can I do to Avoid</span><br><span class="tail">Pressure Ulcers?</span></h1>
    <p class="copy" style="top:78px">There are several ways you can reduce the risk of<br>pressure ulcers.</p>

    <h2 class="topic" style="top:128px">Keep Moving</h2>
    <p class="copy" style="top:158px">Changing your position regularly helps keep<br>blood flowing. If you have reduced movement the<br>Health Care team looking after you will assist you<br>with regular turns in addition to providing special-<br>ist mattresses, cushions, boots etc.</p>

    <h2 class="topic" style="top:266px">Look for signs of Damage</h2>
    <p class="copy" style="top:296px">Check your skin for pressure damage at least once a<br>day. Look for skin that doesn’t go back to its<br>normal colour after you have taken the weight off<br>it. Do not continue to lie on skin that is redder of<br>darker than usual. Also watch out for blisters, dry<br>patches or breaks in the skin.</p>

    <h2 class="topic" style="top:429px">Protect your Skin</h2>
    <p class="copy" style="top:458px">Wash your skin using warm water of PH Neutral<br>skin cleansers. Do not use heavily perfumed soap<br>or talcum powder as these can soak up the skins<br>natural oils leading to vulnerable dry areas. If you<br>suffer from incontinence please inform your<br>health care team as they can assess the best way<br>to deal with the problems. Rubbing/massaging<br>skin is bad for it.</p>

    <h2 class="topic" style="top:635px">Eat a Well-balanced Diet</h2>
    <p class="copy" style="top:664px">Make sure you eat a healthy balanced diet and<br>drink plenty of fluids. Extra protein may help.</p>

    <h2 class="band band--bottom">What should I do if I suspect a<br>pressure ulcer?</h2>
    <p class="copy" style="top:790px">Tell your Doctor or Nurse as soon as possible and<br>follow the advice they give you<br>Rhona Ellery Clinical Nurse Specialist<br>Rhona.ellery@Marlowestaffing.co.uk<br>October 2014</p>
  </section>

  <section class="classification">
    <h2 class="tag tag--classification">Classification of ulcers</h2>

    <p class="stage-label" style="top:140px">Stage <span class="numeral">I</span></p>
    <div class="stage-diagram" style="top:173px;height:128px" role="img" aria-label="Skin cross-section showing stage I pressure ulcer: reddened intact skin"></div>

    <p class="stage-label" style="top:320px">Stage <span class="numeral">II</span></p>
    <div class="stage-diagram" style="top:355px;height:136px" role="img" aria-label="Skin cross-section showing stage II pressure ulcer: shallow open wound"></div>

    <p class="stage-label" style="top:503px">Stage <span class="numeral">III</span></p>
    <div class="stage-diagram" style="top:538px;height:132px" role="img" aria-label="Skin cross-section showing stage III pressure ulcer: full-thickness tissue loss"></div>

    <p class="stage-label" style="top:683px">Stage <span class="numeral">IV</span></p>
    <div class="stage-diagram" style="top:717px;height:147px" role="img" aria-label="Skin cross-section showing stage IV pressure ulcer: deep wound reaching muscle and bone"></div>
  </section>

  <section class="cover">
    <div class="brand">
      <div class="brand-mark"></div>
      <div class="brand-name">Marlowe Staffing</div>
    </div>
    <h1 class="tag tag--leaflet">Pressure Ulcer</h1>
    <div class="talk-icon" role="img" aria-label="Icon of two people in conversation with a speech bubble"></div>
  </section>
</main>
</body>
</html>
```